Thornwell Building Company - advertisement poster

I am looking to print some canvas signs to advertise my general contracting company, Thornwell Building Company. The sign will measure 6' long x 3' high so the size should match that ratio. I already have a logo icon, which is the Letter 'A' and some trees that I would like to incorporate, see attached. I would also like the to have the following information listed:
1) phone number: 472-318-6095
2) email: thornwellbuildingcompany@mailvistra.net
3) website: thornwellbuildingcompany.com
4) Lic#5386204
5) I want to use this text: "BUILD WITH THE T-CREW!"

The ad should be relatively simple and clean. Black and Green are my company colors. I am open to creative ideas!

Target Market(s)

People looking to renovate their homes

Industry/Entity Type

Construction

Colors
59FF00
82FF00
B8FF75
E3FFCB
F4FFEA

Requirements
Must have
• Must have my company logo
Should not have
• No photos or complex graphics

```html
<!DOCTYPE html>
<html lang="en">
<head>
<meta charset="utf-8">
<title>Thornwell Building Company – Sign</title>
<link rel="stylesheet" href="https://fonts.googleapis.com/css2?family=Bebas+Neue&family=Montserrat:ital,wght@0,600;0,700;0,800;1,600&display=swap">
<style>
  :root{
    --green:#70b446;
    --green-dark:#4f8434;
    --black:#000000;
    --white:#ffffff;
    --backdrop:#e4e4e4;
  }
  *{margin:0;padding:0;box-sizing:border-box;}
  html,body{width:1200px;height:718px;overflow:hidden;background:var(--backdrop);}
  .sign{position:absolute;left:20px;top:64px;width:1160px;height:589px;background:var(--green);overflow:hidden;font-family:"Montserrat",sans-serif;}
  .brand-panel{position:absolute;left:5px;top:30px;width:569px;height:554px;background:var(--black);}
  .headline-panel{position:absolute;left:580px;top:0;width:580px;height:330px;background:var(--white);}
  .contact-panel{position:absolute;left:580px;top:336px;width:580px;height:253px;background:var(--black);}
  .house{position:absolute;left:0;top:0;width:1160px;height:330px;}
  .brand-mark{position:absolute;left:242px;top:174px;width:96px;height:96px;border-radius:50%;background:var(--green);}
  .brand-name{position:absolute;left:60px;width:460px;text-align:center;color:var(--white);font-weight:700;}
  .brand-name.primary{top:286px;font-size:44px;letter-spacing:1px;line-height:1;}
  .brand-name.secondary{top:336px;font-size:20px;letter-spacing:7px;line-height:1;}
  .brand-rule{position:absolute;left:204px;top:381px;width:155px;height:2px;background:var(--green);}
  .licence{position:absolute;left:123px;top:415px;width:333px;height:52px;background:var(--green);font-family:"Bebas Neue",sans-serif;font-size:38px;line-height:54px;text-align:center;color:var(--black);letter-spacing:.5px;}
  .licence .number{color:var(--white);}
  .headline{position:absolute;font-family:"Bebas Neue",sans-serif;line-height:1;}
  .headline.build{left:744px;top:124px;font-size:99px;color:var(--white);}
  .headline.with-the{left:924px;top:141px;font-size:43px;color:var(--black);line-height:.85;}
  .headline.crew{left:748px;top:209px;font-size:94px;color:var(--black);}
  .headline-rule{position:absolute;left:745px;top:284px;width:266px;height:3px;background:var(--black);}
  .tool-icon{position:absolute;left:817px;top:76px;width:82px;height:40px;}
  .contact-title{position:absolute;left:599px;top:342px;font-size:31px;font-weight:700;color:var(--green);letter-spacing:-.3px;}
  .contact-icon{position:absolute;border:3px solid var(--green);border-radius:50%;}
  .contact-icon svg{position:absolute;left:50%;top:50%;transform:translate(-50%,-50%);}
  .icon-phone{left:640px;top:396px;width:56px;height:56px;}
  .icon-web{left:644px;top:460px;width:48px;height:48px;}
  .icon-mail{left:644px;top:516px;width:48px;height:48px;}
  .phone{position:absolute;left:718px;top:392px;font-size:61px;font-weight:700;color:var(--white);letter-spacing:-.5px;line-height:1.1;}
  .link{position:absolute;left:718px;font-size:14px;font-style:italic;font-weight:600;color:var(--white);text-transform:uppercase;letter-spacing:.3px;padding-bottom:2px;border-bottom:2px solid var(--green);line-height:1.2;}
  .link.web{top:476px;}
  .link.mail{top:523px;}
</style>
</head>
<body>
<main class="sign">
  <section class="brand-panel"></section>
  <section class="headline-panel"></section>
  <section class="contact-panel"></section>

  <svg class="house" viewBox="0 0 1160 330" aria-hidden="true">
    <polygon points="869,47 1130,150 1067,150 1067,330 668,330 668,150 607,150" fill="#70b446"/>
    <polygon points="869,47 1130,150 1107,150 856,55" fill="#4f8434"/>
    <rect x="1042" y="150" width="25" height="180" fill="#4f8434"/>
  </svg>

  <div class="brand-mark"></div>
  <div class="brand-name primary">THORNWELL</div>
  <div class="brand-name secondary">BUILDING COMPANY</div>
  <div class="brand-rule"></div>
  <div class="licence">LICENCED - <span class="number">5386204</span></div>

  <div class="tool-icon" role="img" aria-label="Hammer icon">
    <svg viewBox="0 0 82 40" width="82" height="40"><rect x="0" y="12" width="82" height="16" rx="8" fill="#000" transform="rotate(-18 41 20)"/></svg>
  </div>
  <div class="headline build">BUILD</div>
  <div class="headline with-the">WITH<br>THE</div>
  <div class="headline crew">T-CREW!</div>
  <div class="headline-rule"></div>

  <h2 class="contact-title">CONTACT US</h2>
  <div class="contact-icon icon-phone">
    <svg width="26" height="26" viewBox="0 0 24 24"><path d="M6.6 10.8a15.2 15.2 0 0 0 6.6 6.6l2.2-2.2a1 1 0 0 1 1-.25 11.4 11.4 0 0 0 3.6.57 1 1 0 0 1 1 1V20a1 1 0 0 1-1 1A17 17 0 0 1 3 4a1 1 0 0 1 1-1h3.5a1 1 0 0 1 1 1c0 1.25.2 2.45.57 3.57a1 1 0 0 1-.25 1z" fill="#fff"/></svg>
  </div>
  <div class="phone">472-318-6095</div>
  <div class="contact-icon icon-web">
    <svg width="24" height="24" viewBox="0 0 24 24" fill="none" stroke="#fff" stroke-width="1.5"><circle cx="12" cy="12" r="9"/><ellipse cx="12" cy="12" rx="4" ry="9"/><path d="M3 12h18M5 7h14M5 17h14"/></svg>
  </div>
  <div class="link web">thornwellbuildingcompany.com</div>
  <div class="contact-icon icon-mail">
    <svg width="26" height="26" viewBox="0 0 26 26"><circle cx="13" cy="13" r="13" fill="#fff"/><rect x="7" y="9" width="12" height="8" fill="none" stroke="#000" stroke-width="1.3"/><path d="M7 9l6 5 6-5" fill="none" stroke="#000" stroke-width="1.3"/></svg>
  </div>
  <div class="link mail">thornwellbuildingcompany@mailvistra.net</div>
</main>
</body>
</html>
```